Australian Conference Brochure

I would like to have a 4 page A4 brochure made up , the product is a service which builds digital libraries for hospital medical equipment instruction manuals ( www.medivantaservices.com.au and www.wardtoolguidevault.com )

I have attached content and order of the brochure to this project ( note pages are mixed up ) the 4th page is attached separately in pdf as it my logo .

The feel for the first page must be along the lines of this link :

http://www.orvellapartners.com/wp-content/uploads/2012/03/0.842.gif

The heading must be pronounced and jump out at you

Pages 2 and 3 must have the same feel as the medivanta services website

The screen shots of the library can be accessed via the library – I can give you access to it for those

The 4 page must be a sketched version of the desktop computer ( see attached pdf ) with 3 instructions manuals coming out of it , with titles :
ICU Ventilator Manufacturers User Troubleshooting Guide
Patient Lift Hoist Manufacturers Set-up Instructions
Diathermy Manufacturers Clinicians Directions for Use
The company logo can be on this page with a info@medivantaservices.com.au e-mail address

Industry/Entity Type

Hospital

```html
<!DOCTYPE html>
<html lang="en">
<head>
<meta charset="utf-8">
<title>MediVanta Services – Compliance Flyer</title>
<link href="https://fonts.googleapis.com/css2?family=Source+Sans+3:ital,wght@0,400;0,600;0,700;1,700&display=swap" rel="stylesheet">
<style>
  :root{
    --wood-light:#c9773a;
    --wood-dark:#9a4f1f;
    --paper:#ffffff;
    --paper-shade:#eef1f4;
    --blue:#2a8fc8;
    --blue-deep:#1e78b0;
    --ink:#333a40;
    --frame:#5a6570;
    --line:#8a8f94;
  }
  *{box-sizing:border-box;margin:0;padding:0}
  html,body{width:873px;height:1200px;overflow:hidden}
  body{font-family:"Source Sans 3",Arial,sans-serif;color:var(--ink);position:relative;
    background:linear-gradient(100deg,var(--wood-dark),var(--wood-light) 30%,#b8652c 55%,var(--wood-light) 80%,var(--wood-dark))}
  .sheet{position:absolute;left:26px;top:26px;width:821px;height:1148px;
    background:linear-gradient(180deg,var(--paper),var(--paper-shade));box-shadow:0 2px 8px rgba(0,0,0,.35)}
  .band{position:absolute;left:26px;width:821px;height:8px;background:var(--blue)}
  .band-top{top:28px}
  .band-bottom{top:1162px}
  .band::after{content:"";position:absolute;left:50%;top:-2px;width:8px;height:12px;background:var(--paper);transform:skewX(-30deg)}
  .abs{position:absolute}
  .hero-art{left:53px;top:42px;width:342px;height:240px;border-radius:6px;
    background:radial-gradient(ellipse at 40% 55%,#b9c3cb,#dfe4e8 55%,rgba(255,255,255,0) 75%)}
  .headline{left:468px;top:100px;width:330px;font-size:17.5px;font-weight:700;line-height:25px;text-align:justify;color:#3a3f44}
  .standards{left:289px;top:306px;width:292px;height:58px;background:var(--blue);color:#fff;
    font-weight:700;font-size:16px;line-height:20px;text-align:center;display:flex;align-items:center;justify-content:center;padding:0 8px}
  .box{position:absolute;background:var(--paper);border:1.5px solid var(--frame);font-size:13.5px;line-height:18.4px}
  .box h3{font-size:13.5px;font-weight:700;color:var(--blue-deep)}
  .guidelines{left:62px;top:404px;width:256px;height:165px;text-align:center;padding:8px 10px}
  .guidelines .accent{color:var(--blue-deep);font-weight:700}
  .nsqhs{left:345px;top:404px;width:473px;height:165px;padding:6px 10px;text-align:justify}
  .nsqhs h3 + p{margin-bottom:14px}
  .criterion{left:62px;top:617px;width:628px;height:163px;padding:5px 8px}
  .criterion .gap{margin-top:16px}
  .doc{top:826px;width:365px;height:194px;text-align:center;padding:8px 12px}
  .doc-2004{left:62px}
  .doc-2012{left:451px}
  .doc .spaced{font-size:11.5px;letter-spacing:3.2px;margin-top:10px;line-height:15px}
  .doc .spaced + .spaced{margin-top:14px}
  .doc h4{font-size:13.5px;color:var(--blue-deep);margin-top:19px}
  .brand{left:62px;top:1062px;display:flex;align-items:center;gap:12px}
  .brand-mark{width:58px;height:58px;background:var(--blue)}
  .brand-name{font-size:30px;font-weight:700;color:var(--blue);line-height:32px;width:160px}
  .contact{left:420px;top:1054px;list-style:none;font-size:24px;font-style:italic;font-weight:700;color:var(--blue-deep)}
  .contact li{display:flex;align-items:center;gap:14px;height:30px}
  .contact svg{flex:none}
</style>
</head>
<body>
  <div class="sheet"></div>
  <div class="band band-top"></div>
  <div class="band band-bottom"></div>

  <div class="abs hero-art" role="img" aria-label="Desktop computer with manuals and books flying out of the screen"></div>

  <p class="abs headline">Every Hospital in Australia and New Zealand has a legal and compliance obligation to make sure all Clinical Staff can access the Manufacturer’s Instructions for Use for equipment they use every day</p>

  <svg class="abs" style="left:0;top:0" width="873" height="1200" aria-hidden="true">
    <g stroke="var(--line)" stroke-width="1.5" fill="none">
      <polyline points="289,336 190,336 190,396"/>
      <polyline points="581,336 677,336 677,396"/>
      <line x1="190" y1="569" x2="190" y2="609"/>
      <line x1="190" y1="780" x2="190" y2="818"/>
      <polyline points="690,758 680,758 680,818"/>
    </g>
    <g fill="var(--line)">
      <polygon points="185,396 195,396 190,404"/>
      <polygon points="672,396 682,396 677,404"/>
      <polygon points="185,609 195,609 190,617"/>
      <polygon points="185,818 195,818 190,826"/>
      <polygon points="675,818 685,818 680,826"/>
    </g>
  </svg>

  <div class="abs standards">National Safety and Quality Health Service (NSQHS) Standards</div>

  <div class="box guidelines">
    <p>HCAB CareAccord Guidelines</p>
    <p class="accent">- Guideline 15 Corporate<br>Systems and Safety</p>
  </div>

  <div class="box nsqhs">
    <h3>National Safety and Quality Health Service Standard 3</h3>
    <p>3.16 Reprocessing reusable medical equipment, instruments and devices in accordance with relevant national or international standards and manufacturers’ instructions.</p>
    <h3>National Safety and Quality Health Service Standard 8</h3>
    <p>8.4.1 Key task : Outputs of improvement processes may include : procedures, protocols and guidelines for the use of and access to equipment</p>
  </div>

  <div class="box criterion">
    <h3>Criterion 15.15.1</h3>
    <p>“ ……..An organisation should have documented management strategies for all medical devices used within its facilities including:</p>
    <p>• medical devices owned, leased or rented by the organisation etc…….</p>
    <p class="gap">AS/NZS 3551:2004 Technical management programs for medical devices67 details for the organisation’s Board, executives and managers the minimum requirements of an effective strategy for the management of medical devices …..”</p>
  </div>

  <div class="box doc doc-2004">
    <h3>AS/NZS 3551:2004</h3>
    <p class="spaced">SECTION2MEDICALDEVICE</p>
    <p class="spaced">MANAGEMENTPROGRAM</p>
    <h4>2.3.4.4 Device-specific documents</h4>
    <p>Documents such as technical and user manuals shall be identified and their locationrecorded in the database.</p>
  </div>

  <div class="box doc doc-2012">
    <h3>AS/NZS 3551:2012</h3>
    <p class="spaced">SECTION2MEDICALDEVICE</p>
    <p class="spaced">MANAGEMENTPROGRAM</p>
    <h4>2.4.3 2.4.3 Supporting documentation</h4>
    <p>Documents such as standards, user guides, technical manuals and other supporting publications shall be identified, stored, issued and updated in a controlled manner.</p>
  </div>

  <div class="abs brand">
    <div class="brand-mark"></div>
    <div class="brand-name">MediVanta Services</div>
  </div>

  <ul class="abs contact">
    <li><svg width="22" height="22" viewBox="0 0 22 22"><circle cx="11" cy="11" r="10" fill="none" stroke="var(--blue-deep)" stroke-width="1.5"/><path d="M7 6c1-1 2 0 2.5 1.5s-1 1.5-.5 2.5 2 2.5 3 3 1-1 2.5-.5 2 1.5 1 2.5-3 1-6-2-3.5-6-2.5-7z" fill="var(--blue-deep)"/></svg>+61 400 555 182</li>
    <li><svg width="22" height="22" viewBox="0 0 22 22"><rect x="3" y="6" width="16" height="11" fill="var(--blue-deep)"/><path d="M3 6l8 6 8-6" fill="none" stroke="#fff" stroke-width="1.3"/></svg>info@medivantaservices.com.au</li>
    <li><svg width="22" height="22" viewBox="0 0 22 22"><g fill="none" stroke="var(--blue-deep)" stroke-width="1.4"><circle cx="11" cy="11" r="8"/><ellipse cx="11" cy="11" rx="3.5" ry="8"/><line x1="3" y1="11" x2="19" y2="11"/></g></svg>www.medivantaservices.com.au</li>
  </ul>
</body>
</html>
```